I need a great design for my Ebook because that will help spread the message

Hey there,

I wrote an eBook (THE MORNING LANTERN METHOD) about how confidence impacts one's life, why it’s important and how to get more of it and I need someone to design it nicely.

My target audience is made up of more women than men.

I have pictures for each one of the 7 steps in the book, but I am open to your suggestions.

I really like Optima as a font. I have a bit of gold in the text. I would be happy if you could keep it. You can format the text as you think best.

I'd love a modern design.

I added an old design of the ebook for you to see the way the pictures are used for each step because I want to keep that blend between the picture and the title of the step.
I like the idea of each step starting on a new page and the block footer - just not black.

I want the subtitle of each step to be a different font to the title.

Please ask any questions you have.

Thank you!

Target Market(s)

Men and women aged 25-45.

Industry/Entity Type

Life Coaching

Font styles to use
Sans Serif

Colors
ffffff

Requirements
Must have
• My brand colours only:
• navy #233264
• white
• light pink #fff3f1
• mustard yellow #ffc800.
Nice to have
• The pictures I uploaded for each step.
Should not have
• Should not have much black.

```html
<!DOCTYPE html>
<html lang="en">
<head>
<meta charset="utf-8">
<title>The Morning Lantern Method – eBook spreads</title>
<link href="https://fonts.googleapis.com/css2?family=Marcellus&family=Tenor+Sans&display=swap" rel="stylesheet">
<style>
  :root{
    --navy:#233264;
    --gold:#ffc800;
    --gold-text:#f2bd1a;
    --blush:#fff3f1;
    --white:#ffffff;
    --ink:#2a2f3d;
    --sky:#6cc3e0;
    --rule:#5a6072;
  }
  *{margin:0;padding:0;box-sizing:border-box}
  html,body{width:1200px;height:1200px;overflow:hidden;background:var(--white)}
  body{position:relative;font-family:"Tenor Sans",sans-serif;color:var(--ink)}
  .page{position:absolute;top:290px;width:374px;height:530px;background:var(--white);
    box-shadow:3px 4px 6px rgba(0,0,0,.35);overflow:hidden}
  .page--cover{left:18px}
  .page--intro{left:414px}
  .page--step{left:807px}

  /* cover */
  .cover-band{position:absolute;left:0;top:0;width:100%;height:350px;background:var(--navy)}
  .cover-accent{position:absolute;left:0;top:347px;width:152px;height:6px;background:var(--gold)}
  .brand{font-family:"Tenor Sans",sans-serif;letter-spacing:.14em;white-space:nowrap}
  .brand b{font-weight:400;letter-spacing:.14em}
  .cover-brand{position:absolute;top:32px;width:100%;text-align:center;color:var(--white);font-size:10px}
  .cover-title{position:absolute;top:193px;width:100%;text-align:center;color:var(--white);
    font-family:"Marcellus",sans-serif;font-size:21px;letter-spacing:.03em;line-height:1}
  .cover-title span{display:block;font-family:"Tenor Sans",sans-serif;font-size:12.5px;letter-spacing:.55em;margin-top:6px;padding-left:.55em}
  .cover-sub{position:absolute;left:30px;top:402px;width:320px;color:var(--gold-text);
    font-size:11.5px;line-height:16px;letter-spacing:.06em;text-transform:uppercase}
  .cover-lead{position:absolute;left:32px;top:455px;width:310px;font-size:7.5px;line-height:10px}

  /* shared */
  .photo{position:absolute;left:0;top:0;width:100%}
  .footer{position:absolute;left:20px;right:22px;bottom:16px;display:flex;align-items:flex-end;gap:6px;font-size:4.5px}
  .footer .line{flex:1;border-bottom:.7px solid var(--rule);height:1px}
  .footer .num{position:absolute;right:0;bottom:3px;color:var(--sky);font-size:4.5px}
  .body-text{font-size:5.6px;line-height:7.1px;text-align:justify}
  .body-text p{margin-bottom:6px}
  .accent-blue{color:var(--sky);letter-spacing:.04em}
  .accent-gold{color:var(--gold-text)}

  /* intro */
  .page--intro .photo{height:270px;
    background:linear-gradient(180deg,#d9d2c6 0%,#e3ddd2 45%,#c9c4bd 70%,rgba(255,255,255,0) 100%)}
  .intro-name{position:absolute;top:282px;width:100%;text-align:center;font-size:17px;color:var(--ink)}
  .intro-bar{position:absolute;top:304px;left:107px;width:152px;height:6px;background:var(--gold)}
  .intro-cols{position:absolute;left:20px;right:22px;top:348px;display:grid;grid-template-columns:1fr 1fr;column-gap:14px}

  /* step */
  .page--step .photo{height:250px;
    background:linear-gradient(180deg,#c9d4d8 0%,#e6dccf 40%,#efe4d7 70%,rgba(255,255,255,0) 100%)}
  .step-label{position:absolute;left:34px;top:188px;color:var(--white);font-family:"Marcellus",sans-serif;font-size:18px;letter-spacing:.06em}
  .step-bar{position:absolute;left:0;top:213px;width:103px;height:5px;background:var(--gold)}
  .step-title{position:absolute;top:244px;width:100%;text-align:center;font-size:10.5px;line-height:16px;letter-spacing:.06em;text-transform:uppercase}
  .step-body{position:absolute;left:22px;right:22px;top:294px}
  .step-body ul{list-style:none;margin-bottom:8px}
</style>
</head>
<body>

<section class="page page--cover">
  <div class="cover-band"></div>
  <div class="cover-accent"></div>
  <div class="cover-brand brand">CLARA<b>VENNER</b></div>
  <h1 class="cover-title">THE MORNING LANTERN<span>METHOD</span></h1>
  <p class="cover-sub">7 steps to becoming the you who achieves their goals, feels fulfilled and loves their life</p>
  <p class="cover-lead">Learn how confidence impacts your life, why its important and how to get more of it</p>
</section>

<section class="page page--intro">
  <div class="photo" role="img" aria-label="Portrait photo of the author in a navy blazer in front of a stone wall, fading into white"></div>
  <div class="intro-name brand">CLARA<b>VENNER</b></div>
  <div class="intro-bar"></div>
  <div class="intro-cols body-text">
    <div>
      <p>What if you could do what you enjoy, have great relationships with the people in your life and feel fulfilled at the end of the day?! Guess what?</p>
      <p class="accent-blue">YOU CAN.</p>
      <p>You can be excited about your work, earn the amount of money you want, be happy in your relationship or enjoy being single, have meaningful friendships, achieve your goals, do the things that bring you to life and absolutely love your life.</p>
      <p class="accent-blue">YOU CAN HAVE IT ALL.</p>
      <p>Whoever said you cant, just didnt know what to do to get there!</p>
    </div>
    <div>
      <p>Growing up, I havent had a good example of having it all. It was either having money - but bad relationships, good relationships - but struggling with finances, money and good relationships but bad health or other combinations that were missing a vital part.<br>Little me didnt want to settle for that. Somewhere in my being, I knew that my life will be what I make it and I would not give up until its just the way I want it. I knew I would have to be relentless, I knew I cant give up, no matter what happens along the way. I also knew that I didnt know so much and that I must keep my curiosity alive to find all the information that I need in order to create my dream life. Dream life may sound far-fetched or even cheesy to some, but I just knew that it is possible to</p>
    </div>
  </div>
  <div class="footer"><span class="brand">CLARA<b>VENNER</b></span><span class="line"></span><span class="num">1</span></div>
</section>

<section class="page page--step">
  <div class="photo" role="img" aria-label="Photo of colourful wooden stacking toys on shelves, fading into white"></div>
  <div class="step-label">STEP 1</div>
  <div class="step-bar"></div>
  <h2 class="step-title">Determine the root cause of your low self -<br>confidence it all stems from your childhood</h2>
  <div class="step-body body-text">
    <p>Perhaps thinking that many confidence issues start from your childhood makes you wonder how this can be possible. Our childhood is often one of the happiest periods in our lives, no worries, no stress, no job, just school and play. There have been many studies on this and research shows that low self-confidence in adult women stems from childhood. Here are two interesting facts that have been revealed:</p>
    <ul class="accent-blue">
      <li>- 30% of young girls are opting out of leadership roles for fear of being called bossy</li>
      <li>- between primary and secondary school, girls self-esteem drops 3.5 times more than boys.</li>
    </ul>
    <p>Were you ever called bossy at a young age? Generally, being called bossy can often be associated with criticism. Young kids can be very passionate about the new things they are learning. They can put a great deal of effort into their projects, both in school and after school activities. Some kids are very outspoken and for that reason they may be called bossy by their colleagues or teachers. This can make them feel like they are doing something wrong, confuse them as to why their hard work is not appreciated or even welcomed. This can also severely affect their determination and diminish their leadership tendencies. This is one of many examples.<br>The reason why this is the first step is because <span class="accent-gold">you have to get to the root</span> cause of your low self-confidence. Dealing with the effects will only keep the issue going, but finding the root cause will help you solve the problem once and for all.<br>Here are several questions to ask yourself to help you identify what particular situations have left a negative mark on you. Write down the answers, as detailed as possible so that you can revisit them.</p>
    <p class="accent-blue">In a confrontation, did you stand up for yourself or did you let people get away with it?<br>Who was your favourite person growing up? What was your relationship with them like?<br>When you werent happy with a situation, did you talk to anyone about it?</p>
  </div>
  <div class="footer"><span class="brand">CLARA<b>VENNER</b></span><span class="line"></span><span class="num">1</span></div>
</section>

</body>
</html>
```